Weddings by Mirela
Wedding Planner
I NEED CONCEPTS WITH ENVELOPE, BUSINESS CARD AND PAPER...
NOT ONLY BUSINESS CARDS
THANK YOU
Hi everyone
thanks for sending.
please don't add Switzerland / schweiz...
i dont need to have the country on my business card. thanks a bunch. i am sorting out and get back to you now...
Designers: Logo .AI has been uploaded. Kindly refer to the creative brief. - Dean Pruitt
my logo should be there now....
thanks for drafts
plz upload the logo
My logo should be on business cards, letters and envelopes...
Writings should be same as used in my logo. Except if you add the address it should be kindof a "normal" writing.
i think it would look stupid if it will be same as in logo...
for questions, pls send message
cheers

```html
<!DOCTYPE html>
<html lang="en">
<head>
<meta charset="utf-8">
<title>Weddings by Mirela – Stationery</title>
<link href="https://fonts.googleapis.com/css2?family=Lato:wght@400;700&display=swap" rel="stylesheet">
<style>
  :root{
    --gold:#c9a13f;
    --gold-light:#e6c877;
    --gold-dark:#a87e26;
    --orange:#c98a2e;
    --cream:#f6e2b4;
    --grey-dark:#8f8f8f;
    --grey-light:#ececec;
    --paper:#ffffff;
    --edge:#bdbdbd;
    --ink:#333333;
    --bg:#ffffff;
  }
  *{box-sizing:border-box;margin:0;padding:0}
  html,body{width:1200px;height:744px;overflow:hidden;background:var(--bg)}
  .canvas{position:relative;width:1200px;height:744px;font-family:'Lato',Arial,sans-serif}
  .piece{position:absolute;background:var(--paper);border:1px solid var(--edge);overflow:hidden}
  .piece svg.band{position:absolute;left:0;top:0;width:100%;height:100%}
  .brand{position:absolute;display:flex;align-items:center;gap:0.35em;font-family:'Lato',Arial,sans-serif;font-weight:400;color:var(--gold);white-space:nowrap;line-height:1}
  .brand .dot{display:inline-block;width:0.55em;height:0.55em;border-radius:50%;background:currentColor}
  .small{position:absolute;line-height:1.45;color:var(--ink);white-space:nowrap}

  /* letterhead */
  .letterhead{left:29px;top:29px;width:513px;height:686px}
  .letterhead .brand{left:24px;top:84px;font-size:26px}
  .letterhead .contact{right:18px;top:18px;text-align:right;color:#fff;font-size:8px}

  /* business card front */
  .card-front{left:571px;top:29px;width:221px;height:120px}
  .card-front .brand{left:12px;top:28px;font-size:12px}
  .card-front .person{left:124px;top:50px;font-size:6.5px}
  .card-front .details{left:12px;top:78px;font-size:5.5px}

  /* business card back */
  .card-back{left:835px;top:72px;width:221px;height:125px;border-color:#d0d0d0}
  .card-back .brand{left:50%;top:50%;transform:translate(-50%,-50%);font-size:15px}

  /* grey card */
  .card-grey{left:605px;top:216px;width:216px;height:125px;border:none;background:linear-gradient(180deg,var(--grey-dark) 0%,#b9b9b9 55%,var(--grey-light) 100%)}
  .card-grey .brand{left:50%;top:50%;transform:translate(-50%,-50%);font-size:15px;color:var(--gold-light)}

  /* orange card */
  .card-orange{left:869px;top:235px;width:225px;height:125px;border:1px solid #b07622;background:linear-gradient(180deg,#d59a3c,var(--orange))}
  .card-orange .brand{left:50%;top:50%;transform:translate(-50%,-50%);font-size:15px;color:var(--cream)}

  /* envelope */
  .envelope{left:571px;top:379px;width:605px;height:341px}
  .envelope .brand{left:18px;top:150px;font-size:24px}
  .envelope .country{left:44px;top:190px;font-size:8px}
</style>
</head>
<body>
<div class="canvas">

  <section class="piece letterhead" aria-label="Letterhead">
    <svg class="band" viewBox="0 0 513 686" preserveAspectRatio="none" aria-hidden="true">
      <defs>
        <linearGradient id="lhGold" x1="0" x2="1" y1="0" y2="0">
          <stop offset="0" stop-color="#e6c877"/>
          <stop offset="0.5" stop-color="#c9a13f"/>
          <stop offset="1" stop-color="#a87e26"/>
        </linearGradient>
      </defs>
      <path d="M0 0H513V150C430 118 340 62 230 50C140 40 60 44 0 42Z" fill="url(#lhGold)"/>
      <path d="M0 50C60 52 140 48 230 58C340 70 430 126 513 158" fill="none" stroke="#c9a13f" stroke-width="1.5"/>
    </svg>
    <div class="brand">Weddings by Mirela <span class="dot"></span></div>
    <div class="small contact">
      Schweiz / Switzerland<br>
      Phone: +41 79 512 38 04<br>
      Email: info@weddingsbymirela.ch<br>
      www.weddingsbymirela.ch
    </div>
  </section>

  <section class="piece card-front" aria-label="Business card front">
    <svg class="band" viewBox="0 0 221 120" preserveAspectRatio="none" aria-hidden="true">
      <defs>
        <linearGradient id="bcGold" x1="0" x2="1">
          <stop offset="0" stop-color="#e6c877"/>
          <stop offset="1" stop-color="#a87e26"/>
        </linearGradient>
      </defs>
      <path d="M0 0H221V22C170 14 120 8 70 12C40 14 20 16 0 18Z" fill="url(#bcGold)"/>
      <path d="M0 22C30 19 60 16 90 16C140 16 180 22 221 28" fill="none" stroke="#c9a13f" stroke-width="0.8"/>
    </svg>
    <div class="brand">Weddings by Mirela <span class="dot"></span></div>
    <div class="small person">Mirela Ostrov-Keller<br>Wedding Planner</div>
    <div class="small details">
      Natel: +41 79 512 38 04<br>
      Phone: +41 44 310 22 18<br>
      Email: info@weddingsbymirela.ch<br>
      www.weddingsbymirela.ch
    </div>
  </section>

  <section class="piece card-back" aria-label="Business card back">
    <div class="brand">Weddings by Mirela <span class="dot"></span></div>
  </section>

  <section class="piece card-grey" aria-label="Business card, grey variant">
    <div class="brand">Weddings by Mirela <span class="dot"></span></div>
  </section>

  <section class="piece card-orange" aria-label="Business card, orange variant">
    <div class="brand">Weddings by Mirela <span class="dot"></span></div>
  </section>

  <section class="piece envelope" aria-label="Envelope">
    <svg class="band" viewBox="0 0 605 341" preserveAspectRatio="none" aria-hidden="true">
      <defs>
        <linearGradient id="envGold" x1="0" x2="1">
          <stop offset="0" stop-color="#e6c877"/>
          <stop offset="0.5" stop-color="#c9a13f"/>
          <stop offset="1" stop-color="#a87e26"/>
        </linearGradient>
      </defs>
      <path d="M0 0H605V80C500 92 330 138 170 130C90 126 40 118 0 112Z" fill="url(#envGold)"/>
      <path d="M0 120C40 126 90 134 170 138C330 146 500 100 605 88" fill="none" stroke="#c9a13f" stroke-width="1.5"/>
    </svg>
    <div class="brand">Weddings by Mirela <span class="dot"></span></div>
    <div class="small country">Schweiz / Switzerland</div>
  </section>

</div>
</body>
</html>
```